Q&L Summit Holdings Business Cards

Design Business cards in a format where I can change the information and utilize a third party buisness card printing company

Contact Information for Business Card

Want Logo and Name on Back. Looking for Spot UV style shine on Logo. Probably Black background. Want smaller logo on front with contact details. Like rounded edges or something else interesting.

Requirements
Must have
• Strong masculine look.

```html
<!DOCTYPE html>
<html lang="en">
<head>
<meta charset="utf-8">
<title>Q&amp;L Summit Holdings Business Cards</title>
<link rel="stylesheet" href="https://fonts.googleapis.com/css2?family=Cinzel:wght@400;600;700&display=swap">
<style>
  :root {
    --stage: #1e1e20;
    --card-dark: #0f0f10;
    --card-dark-edge: #1b1b1d;
    --card-light: #f1f1ef;
    --brand-grey-dark: #8c8c8e;
    --brand-grey-light: #77777a;
    --ink: #4a4a4d;
    --ink-soft: #5c5c60;
    --rule: #8d8d90;
  }
  * { box-sizing: border-box; margin: 0; padding: 0; }
  html, body {
    width: 1200px; height: 900px; overflow: hidden;
    background: var(--stage);
    font-family: "Cinzel", "Times New Roman", serif;
  }
  .stage {
    position: relative; width: 1200px; height: 900px;
    display: flex; flex-direction: column; align-items: center;
    justify-content: center; gap: 30px;
  }
  .card {
    width: 700px; height: 400px; border-radius: 6px;
    position: relative; overflow: hidden;
  }
  .card--back {
    background: linear-gradient(135deg, var(--card-dark-edge), var(--card-dark) 60%);
    display: flex; align-items: center; justify-content: center;
  }
  .card--back .brand-name {
    color: var(--brand-grey-dark);
    font-size: 44px; font-weight: 600; letter-spacing: 1px;
    text-align: center; line-height: 1.15; width: 420px;
  }
  .card--front {
    background: var(--card-light);
    display: flex; align-items: center;
  }
  .front-brand {
    width: 330px; display: flex; justify-content: center;
  }
  .front-brand .brand-name {
    color: var(--brand-grey-light);
    font-size: 38px; font-weight: 600; line-height: 1.15;
    text-align: center; width: 260px;
  }
  .divider {
    width: 2px; height: 250px; background: var(--rule);
  }
  .contact {
    padding-left: 28px; color: var(--ink);
  }
  .contact .person {
    font-size: 30px; font-weight: 700; letter-spacing: 1px; color: var(--ink);
  }
  .contact .role {
    font-size: 16px; color: var(--ink-soft); margin-top: -2px;
  }
  .contact .address {
    font-size: 17px; margin-top: 20px; line-height: 1.3;
  }
  .contact .lines { margin-top: 14px; list-style: none; }
  .contact .lines li {
    display: flex; align-items: center; gap: 10px;
    font-size: 17px; line-height: 1.5;
  }
  .contact .lines svg { width: 14px; height: 14px; flex: none; }
</style>
</head>
<body>
<main class="stage">
  <section class="card card--back" aria-label="Card back">
    <p class="brand-name">Q&amp;L Summit Holdings</p>
  </section>

  <section class="card card--front" aria-label="Card front">
    <div class="front-brand">
      <p class="brand-name">Q&amp;L Summit Holdings</p>
    </div>
    <div class="divider"></div>
    <div class="contact">
      <p class="person">Daniel Reeve</p>
      <p class="role">Director</p>
      <p class="address">12345 Address Street<br>City State Postcode Country</p>
      <ul class="lines">
        <li>
          <svg viewBox="0 0 16 16" aria-hidden="true"><path d="M4 1.5l2.2 3-1.3 1.6a8 8 0 0 0 5 5l1.6-1.3 3 2.2-1.2 2.3c-5.5 0-11.3-5.8-11.3-11.3z" fill="none" stroke="#555" stroke-width="1.4" stroke-linejoin="round"/></svg>
          +330 2460-5173
        </li>
        <li>
          <svg viewBox="0 0 16 16" aria-hidden="true"><rect x="1.5" y="3.5" width="13" height="9" fill="none" stroke="#555" stroke-width="1.4"/><path d="M1.5 3.5L8 9l6.5-5.5" fill="none" stroke="#555" stroke-width="1.4"/></svg>
          info@qlsummitholdings.com
        </li>
        <li>
          <svg viewBox="0 0 16 16" aria-hidden="true"><circle cx="8" cy="8" r="6.5" fill="none" stroke="#555" stroke-width="1.3"/><ellipse cx="8" cy="8" rx="2.8" ry="6.5" fill="none" stroke="#555" stroke-width="1.1"/><path d="M1.5 8h13M2.6 4.8h10.8M2.6 11.2h10.8" stroke="#555" stroke-width="1"/></svg>
          www.qlsummitholdings.com
        </li>
      </ul>
    </div>
  </section>
</main>
</body>
</html>
```